Four Paths to Thriving icons

We are a workplace wellbeing company and have created a challenge around the four paths to thriving - Be Active, Give, Keep Learning, Take Notice and Connect. We would like to brand our own icons around these 5 ways. We would like them with tag lines and without please.
Please see how these are used by others to show you what I mean. https://www.findzoria.example/search?q=four+paths+to+thriving&mode=img&ref=Qx7Lm2Pz9TkR4vBn8WcY3hJd6FsA1eUo&w=1440&h=738
We would like to use the colours based on the Tarvin Mind Care society:
Connect - Engage with others (Teal)
Be Active - Get moving (Purple)
Keep Learning - Expand your mind - Green
Take Notice - Slow down and focus - Orange
Give - Be there for others - Pink
We would like something fun, vibrant, fresh, professional
Please see our company logo and website - www.staffvitalux.example

```html
<!DOCTYPE html>
<html lang="en">
<head>
<meta charset="utf-8">
<title>Four Paths to Thriving</title>
<link rel="stylesheet" href="https://fonts.googleapis.com/css2?family=Oswald:wght@500&display=swap">
<style>
  :root {
    --frame: #a7a8aa;
    --backdrop: #e8e9eb;
    --scene: #dfe0e2;
    --teal: #4fa8b8;
    --purple: #9b4f9f;
    --green: #86c35f;
    --orange: #f4a240;
    --pink: #ed3f8f;
    --ink: #ffffff;
  }
  html, body {
    margin: 0;
    padding: 0;
    overflow: hidden;
    background: var(--frame);
  }
  .canvas {
    position: relative;
    width: 1200px;
    height: 849px;
    background: var(--frame);
    overflow: hidden;
  }
  .poster {
    display: block;
    width: 1200px;
    height: 849px;
  }
  .backdrop { fill: var(--backdrop); }
  .office-scene { fill: var(--scene); }
  .path-oval { fill-opacity: 0.86; }
  .path-oval--connect { fill: var(--teal); }
  .path-oval--active { fill: var(--purple); }
  .path-oval--learning { fill: var(--green); }
  .path-oval--notice { fill: var(--orange); }
  .path-oval--give { fill: var(--pink); }
  .path-icon { fill: var(--ink); fill-opacity: 0.85; }
  .path-label {
    font-family: "Oswald", sans-serif;
    font-weight: 500;
    font-size: 24px;
    letter-spacing: 1px;
    fill: var(--ink);
    text-anchor: middle;
  }
</style>
</head>
<body>
<main class="canvas">
  <svg class="poster" viewBox="0 0 1200 849" xmlns="http://www.w3.org/2000/svg">
    <rect class="frame" x="0" y="0" width="1200" height="849" fill="var(--frame)"/>
    <rect class="backdrop" x="29" y="29" width="1142" height="791"/>

    <g role="img" aria-label="Faint office illustration: wall clock, desk, chair, a thinking worker and floating question marks">
      <rect class="office-scene" x="29" y="29" width="1142" height="791" fill-opacity="0.5"/>
    </g>

    <g class="paths">
      <ellipse class="path-oval path-oval--connect" cx="264" cy="334" rx="118" ry="150" transform="rotate(-22 264 334)"/>
      <ellipse class="path-oval path-oval--active" cx="470" cy="334" rx="118" ry="150" transform="rotate(-22 470 334)"/>
      <ellipse class="path-oval path-oval--learning" cx="686" cy="334" rx="118" ry="150" transform="rotate(-22 686 334)"/>
      <ellipse class="path-oval path-oval--notice" cx="894" cy="334" rx="118" ry="150" transform="rotate(-22 894 334)"/>
      <ellipse class="path-oval path-oval--give" cx="583" cy="526" rx="157" ry="116"/>
    </g>

    <g class="icons">
      <rect class="path-icon" x="208" y="232" width="112" height="142" rx="40" role="img" aria-label="Icon: two leaf-shaped hands reaching toward each other"/>
      <rect class="path-icon" x="384" y="242" width="172" height="118" rx="40" role="img" aria-label="Icon: running figure with a sweeping motion line"/>
      <rect class="path-icon" x="610" y="242" width="134" height="120" rx="16" role="img" aria-label="Icon: open book on a computer screen"/>
      <rect class="path-icon" x="816" y="246" width="184" height="112" rx="50" role="img" aria-label="Icon: camera aperture eye between angle brackets"/>
      <rect class="path-icon" x="494" y="460" width="178" height="100" rx="40" role="img" aria-label="Icon: open hand holding a heart"/>
    </g>

    <g class="labels">
      <text class="path-label" x="266" y="407">CONNECT</text>
      <text class="path-label" x="469" y="407">BE ACTIVE</text>
      <text class="path-label" x="688" y="407">KEEP LEARNING</text>
      <text class="path-label" x="896" y="407">TAKE NOTICE</text>
      <text class="path-label" x="583" y="611">GIVE</text>
    </g>
  </svg>
</main>
</body>
</html>
```